Business Card Design

Recruitment Company. Want to keep the logo and the green colour

Industry/Entity Type

Business

Contact Information for Business Card

Hi,

1.)
MARTIN HOLLOWAY
Director
Level 6, 248 Finch Street
Brisbane QLD 4000
M 0412 630 574
E martin@tallonstaffing.com.au
www.tallonstaffing.com.au

2.)
TOM WAVERLEY
Director
Level 6, 248 Finch Street
Brisbane QLD 4000
M 0419 247 613
E tom@tallonstaffing.com.au

Want something different and eye catching, happy for you guys to use your design flare to work some magic with these.

Many Thanks
Tom

```html
<!DOCTYPE html>
<html lang="en">
<head>
<meta charset="utf-8">
<title>Tallon Staffing – Business Card</title>
<link href="https://fonts.googleapis.com/css2?family=Arimo:wght@400;700&display=swap" rel="stylesheet">
<style>
  :root {
    --page-bg: #e9e9e7;
    --card-white: #ffffff;
    --brand-green: #3fb44a;
    --green-deep: #1fae4b;
    --green-light: #a8d84a;
    --text-dark: #1f2a1c;
    --text-white: #ffffff;
    --card-shadow: rgba(0, 0, 0, 0.14);
  }
  * { margin: 0; padding: 0; box-sizing: border-box; }
  html, body {
    width: 1200px;
    height: 856px;
    overflow: hidden;
    background: var(--page-bg);
    font-family: "Arimo", Arial, sans-serif;
  }
  .canvas {
    position: relative;
    width: 1200px;
    height: 856px;
  }
  .card {
    position: absolute;
    top: 275px;
    width: 500px;
    height: 306px;
    border-radius: 34px;
    box-shadow: 0 6px 18px var(--card-shadow);
    overflow: hidden;
  }
  /* Front side: white with brand name */
  .card-front {
    left: 70px;
    background: var(--card-white);
    display: flex;
    align-items: center;
    justify-content: center;
    gap: 14px;
  }
  .brand-dot {
    width: 26px;
    height: 26px;
    border-radius: 50%;
    background: var(--brand-green);
  }
  .brand-name {
    color: var(--brand-green);
    font-weight: 700;
    font-size: 46px;
    letter-spacing: -0.5px;
  }
  /* Back side: green gradient with contact details */
  .card-back {
    left: 630px;
    background: linear-gradient(120deg, var(--green-deep) 0%, #5cc144 40%, var(--green-light) 65%, var(--green-deep) 100%);
    display: flex;
    align-items: center;
    padding: 0 30px 0 36px;
    gap: 24px;
  }
  .back-brand {
    width: 130px;
    color: var(--text-white);
    font-weight: 700;
    font-size: 24px;
    line-height: 1.1;
    text-align: center;
  }
  .contact {
    color: var(--text-dark);
    font-size: 15px;
    font-weight: 700;
    line-height: 1.28;
  }
  .contact-name {
    color: var(--text-white);
    font-weight: 700;
    font-size: 15px;
  }
  .contact-role {
    color: var(--text-white);
    font-weight: 400;
    font-size: 13px;
    margin-bottom: 12px;
  }
</style>
</head>
<body>
  <main class="canvas">
    <section class="card card-front" aria-label="Card front">
      <span class="brand-dot" aria-hidden="true"></span>
      <span class="brand-name">tallon staffing</span>
    </section>

    <section class="card card-back" aria-label="Card back">
      <div class="back-brand">tallon staffing</div>
      <div class="contact">
        <p class="contact-name">MARTIN HOLLOWAY</p>
        <p class="contact-role">Director</p>
        <p>Level 6,</p>
        <p>248 Finch Street Brisbane</p>
        <p>QLD 4000</p>
        <p>M 0412 630 574 E</p>
        <p>martin@tallonstaffing.com.au</p>
        <p>www.tallonstaffing.com.au</p>
      </div>
    </section>
  </main>
</body>
</html>
```